Marnie's Hideaway Flyer

Need an attractive flyer for an existing Spa in SG around the Quillbrook area ( Former Elm Hall) . Our spa is s converted horse stables , environment totally back to nature - see horse riding etc...even though it is located in the suburbs
Main business come from facials, waxing/hair removals, instant spraytan and body works. Flyer needs to attract new clients to our business.
Updates

Target Market(s)

Adults of 25 -65 ( male and female), English speaking

Industry/Entity Type

Environment

Font styles to use
Script

Requirements
Must have
• Must have the 5 logos of the top brand products we use in the Spa.
Should not have
• No tacky designs. Must maintain class and decorum .
No animations too.

```html
<!DOCTYPE html>
<html lang="en">
<head>
<meta charset="utf-8">
<title>Marnie's Hideaway Flyer</title>
<link href="https://fonts.googleapis.com/css2?family=Open+Sans:wght@400;600&family=Great+Vibes&display=swap" rel="stylesheet">
<style>
  :root {
    --red: #c1272d;
    --red-deep: #a61d24;
    --ink: #2b2b2b;
    --grey-text: #6d6e71;
    --grey-soft: #9a9b9e;
    --grey-band: #a7a9ac;
    --paper: #ffffff;
    --paper-shade: #eeeff0;
    --skin-light: #f3dccb;
    --skin-mid: #d9ab8e;
  }
  * { margin: 0; padding: 0; box-sizing: border-box; }
  html, body { width: 786px; height: 1200px; overflow: hidden; background: var(--paper); }
  body { font-family: "Open Sans", Arial, sans-serif; }
  .flyer {
    position: relative; width: 786px; height: 1200px; overflow: hidden;
    background: linear-gradient(180deg, var(--paper) 0%, var(--paper) 38%, var(--paper-shade) 62%, var(--paper) 90%);
  }
  .hero-photo {
    position: absolute; left: 40px; top: 0; width: 620px; height: 470px;
    background: radial-gradient(ellipse at 40% 45%, var(--skin-light) 0%, var(--skin-mid) 45%, rgba(255,255,255,0) 72%);
  }
  .hero-curves { position: absolute; left: 0; top: 220px; width: 786px; height: 290px; }
  .brand-name {
    position: absolute; left: 404px; top: 82px; width: 360px;
    font-size: 37px; font-weight: 400; color: var(--ink); text-align: center; letter-spacing: 0.5px;
  }
  .tagline {
    position: absolute; left: 380px; top: 166px; width: 380px; text-align: center;
    font-family: "Great Vibes", cursive; font-size: 27px; color: var(--grey-soft);
  }
  .headline {
    position: absolute; left: 0; top: 496px; width: 786px; text-align: center;
    color: var(--red); font-size: 24px; line-height: 39px; text-transform: uppercase; font-weight: 400;
  }
  .services {
    position: absolute; left: 0; top: 596px; width: 786px;
    display: flex; justify-content: center; align-items: center; gap: 12px;
    color: var(--grey-text); font-size: 28px;
  }
  .services .dot { display: inline-block; width: 4px; height: 10px; background: var(--grey-text); transform: skewX(-20deg); border-radius: 2px; }
  .gallery { position: absolute; top: 655px; left: 48px; width: 694px; display: flex; justify-content: space-between; }
  .gallery-tile { width: 208px; height: 133px; border: 2px solid #d3d4d6; }
  .tile-facial { background: linear-gradient(135deg, #e9e4dc, #c9ad98); }
  .tile-body { background: linear-gradient(135deg, #fbf3ea, #e6c2a5); }
  .tile-nails { background: linear-gradient(135deg, #f1d8cc, #d9a991); }
  .pitch {
    position: absolute; left: 0; top: 812px; width: 786px; text-align: center;
    color: var(--red); font-size: 21px; line-height: 31px;
  }
  .hours {
    position: absolute; left: 0; top: 896px; width: 786px; text-align: center;
    color: var(--grey-soft); font-size: 19px; line-height: 31px;
  }
  .website {
    position: absolute; left: 0; top: 975px; width: 786px;
    display: flex; justify-content: center; align-items: center; gap: 14px;
    color: var(--red); font-size: 27px;
  }
  .website svg { width: 30px; height: 30px; }
  .outlets { position: absolute; left: 30px; top: 1072px; color: var(--ink); font-size: 19px; }
  .phone-tab { position: absolute; left: 469px; top: 1000px; width: 317px; height: 122px; }
  .phone-number {
    position: absolute; left: 540px; top: 1052px;
    display: flex; align-items: center; gap: 14px; color: #fff; font-size: 34px;
  }
  .phone-number svg { width: 34px; height: 34px; }
  .partner-bar {
    position: absolute; left: 0; top: 1122px; width: 786px; height: 78px; background: var(--grey-band);
    display: flex; justify-content: space-around; align-items: center; padding: 0 18px;
  }
  .partner-name { font-size: 24px; font-weight: 600; color: #3a3a3a; letter-spacing: 1px; }
</style>
</head>
<body>
<main class="flyer">
  <div class="hero-photo" role="img" aria-label="Photo of a relaxed woman resting her head on her arms, holding a pink lotus flower"></div>

  <svg class="hero-curves" viewBox="0 0 786 290" aria-hidden="true">
    <path d="M0 70 C120 190 260 250 420 245 C560 240 660 160 786 150 L786 290 L0 290 Z" fill="#f4f4f5"/>
    <path d="M0 70 C120 190 260 250 420 245 C560 240 660 160 786 150 L786 166 C660 176 560 256 420 260 C250 266 110 205 0 100 Z" fill="var(--red)"/>
    <path d="M0 104 C110 210 250 272 420 266 C560 262 660 182 786 172" fill="none" stroke="#b8b9bb" stroke-width="3"/>
  </svg>

  <div class="brand-name">Marnie's Hideaway</div>
  <div class="tagline">The One-stop Salon / Spa of Choice</div>

  <h1 class="headline">Looking and feeling good doesn't need<br>to be your little secret.</h1>

  <div class="services">
    <span class="dot"></span><span>Waxing</span>
    <span class="dot"></span><span>Nails</span>
    <span class="dot"></span><span>Spraytan</span>
    <span class="dot"></span><span>Face</span>
    <span class="dot"></span><span>Body</span>
    <span class="dot"></span>
  </div>

  <div class="gallery">
    <div class="gallery-tile tile-facial" role="img" aria-label="Photo of a woman with a towel wrap and a face mask"></div>
    <div class="gallery-tile tile-body" role="img" aria-label="Photo of a woman with smooth shoulders and arms"></div>
    <div class="gallery-tile tile-nails" role="img" aria-label="Photo of manicured hands and pedicured feet"></div>
  </div>

  <p class="pitch">From facials, Brazilian waxing to nails and body,<br>Marnie's Hideaway will always make you feel pampered...</p>
  <p class="hours">We are open daily.<br>Call in for special deals at the spa, or visit our website at:</p>

  <div class="website">
    <svg viewBox="0 0 30 30" aria-hidden="true">
      <circle cx="14" cy="14" r="12" fill="none" stroke="var(--red)" stroke-width="3"/>
      <path d="M2 14 H26 M14 2 C8 8 8 20 14 26 M14 2 C20 8 20 20 14 26" fill="none" stroke="var(--red)" stroke-width="2"/>
      <path d="M16 16 L28 22 L22 23 L20 29 Z" fill="var(--red)" stroke="#fff" stroke-width="1.5"/>
    </svg>
    <span>www.marnieshideaway.sg</span>
  </div>

  <p class="outlets">Outlets: 100 Elm Hall Road, #01-02c Stablegate</p>

  <svg class="phone-tab" viewBox="0 0 317 122" aria-hidden="true">
    <path d="M0 122 C10 40 120 10 317 0 L317 122 Z" fill="var(--red)"/>
  </svg>
  <div class="phone-number">
    <svg viewBox="0 0 34 34" aria-hidden="true">
      <path d="M4 12 C4 6 30 6 30 12 L30 15 L24 15 L24 12 L10 12 L10 15 L4 15 Z" fill="#fff"/>
      <path d="M9 17 L25 17 L29 30 L5 30 Z" fill="#fff"/>
      <circle cx="17" cy="23" r="3.5" fill="var(--red)"/>
    </svg>
    <span>6100 2470</span>
  </div>

  <div class="partner-bar">
    <span class="partner-name">Lumeva</span>
    <span class="partner-name">Orvelle</span>
    <span class="partner-name">Castine</span>
    <span class="partner-name">Belrose</span>
    <span class="partner-name">Kaiyo</span>
  </div>
</main>
</body>
</html>
```